Brisk Tailor Signage

This design is for "signage" that we intend to get produced.
A couple of different designs that say "Brisk Tailor on Guard" and "Beware of Brisk Tailor"
It should also have our logo (BT) plus our logo with the hand and dog paw. We would also like the main picture of the sign to be the attached. We would like a classy sophisticated look similar to our logo you designed.
Our designs will go on consumers gates/entrances to warn people there is a dog on the premises. I will get a better quality picture of the dog.

```html
<!DOCTYPE html>
<html lang="en">
<head>
<meta charset="utf-8">
<title>Brisk Tailor Signage</title>
<link href="https://fonts.googleapis.com/css2?family=Marcellus&display=swap" rel="stylesheet">
<style>
  :root {
    --backdrop: #cecece;
    --sign: #ffffff;
    --ink: #231f20;
    --paper: #ffffff;
    --portrait-light: #f4f4f4;
    --portrait-shade: #b9b9b9;
  }
  html, body {
    margin: 0;
    padding: 0;
    width: 1200px;
    height: 1200px;
    overflow: hidden;
    background: var(--backdrop);
  }
  .canvas { display: block; width: 1200px; height: 1200px; }
  .sign-board { fill: var(--sign); }
  .sign-frame { fill: none; stroke: var(--ink); stroke-width: 5; stroke-linecap: round; }
  .dome { fill: var(--ink); }
  .dog-portrait { fill: url(#portraitTone); stroke: var(--paper); stroke-width: 6; }
  .headline {
    font-family: "Marcellus", serif;
    fill: var(--ink);
    letter-spacing: 2px;
  }
  .name-band { fill: var(--ink); }
  .name-band-rule { fill: none; stroke: var(--paper); stroke-width: 2; }
  .brand-dot { fill: var(--paper); stroke: var(--ink); stroke-width: 3; }
  .brand-name {
    font-family: "Marcellus", serif;
    fill: var(--paper);
  }
</style>
</head>
<body>
<svg class="canvas" viewBox="0 0 1932 1932" xmlns="http://www.w3.org/2000/svg">
  <defs>
    <linearGradient id="portraitTone" x1="0" y1="0" x2="0" y2="1">
      <stop offset="0" stop-color="var(--portrait-light)"/>
      <stop offset="1" stop-color="var(--portrait-shade)"/>
    </linearGradient>
    <g id="frame" class="sign-frame">
      <path d="M510,227 V211 Q510,181 540,181 H1393 Q1423,181 1423,211 V227"/>
      <path d="M525,211 Q479,211 479,257 V840 Q479,886 525,886"/>
      <path d="M1408,211 Q1455,211 1455,257 V840 Q1455,886 1408,886"/>
      <path d="M510,870 V886 Q510,916 540,916 H1393 Q1423,916 1423,886 V870"/>
      <circle cx="525" cy="227" r="16"/>
      <circle cx="1408" cy="227" r="16"/>
      <circle cx="525" cy="870" r="16"/>
      <circle cx="1408" cy="870" r="16"/>
    </g>
  </defs>

  <!-- Sign: Beware of -->
  <g class="sign sign-beware">
    <rect class="sign-board" x="445" y="147" width="1043" height="803"/>
    <use href="#frame"/>
    <path class="dome" d="M699,575 A267,267 0 0 1 1234,575 Z"/>
    <path class="dog-portrait" role="img" aria-label="Line drawing of an alert dog with upright ears"
          d="M835,575 V300 Q835,232 900,232 H1070 Q1135,232 1135,300 V575 Z"/>
    <text class="headline" x="966" y="693" font-size="136" text-anchor="middle" textLength="750" lengthAdjust="spacingAndGlyphs">BEWARE OF</text>
    <rect class="name-band" x="640" y="717" width="653" height="121" rx="60"/>
    <rect class="name-band-rule" x="648" y="725" width="637" height="105" rx="52"/>
    <circle class="brand-dot" cx="699" cy="778" r="50"/>
    <circle class="brand-dot" cx="1233" cy="778" r="50"/>
    <text class="brand-name" x="966" y="800" font-size="64" text-anchor="middle">Brisk Tailor</text>
  </g>

  <!-- Sign: On guard -->
  <g class="sign sign-on-guard" transform="translate(0,836)">
    <rect class="sign-board" x="445" y="147" width="1043" height="803"/>
    <use href="#frame"/>
    <path class="dome" d="M699,587 A267,267 0 0 1 1234,587 Z"/>
    <path class="dog-portrait" role="img" aria-label="Line drawing of a floppy-eared hound"
          d="M790,587 V330 Q790,244 880,244 H1060 Q1150,244 1150,330 V587 Z"/>
    <rect class="name-band" x="600" y="610" width="733" height="137" rx="68"/>
    <rect class="name-band-rule" x="609" y="619" width="715" height="119" rx="59"/>
    <circle class="brand-dot" cx="668" cy="678" r="56"/>
    <circle class="brand-dot" cx="1265" cy="678" r="56"/>
    <text class="brand-name" x="966" y="702" font-size="70" text-anchor="middle">Brisk Tailor</text>
    <text class="headline" x="966" y="852" font-size="120" text-anchor="middle" textLength="617" lengthAdjust="spacingAndGlyphs">ON GUARD</text>
  </g>
</svg>
</body>
</html>
```